Corvelle Beauty Lounge needs a product poster

This poster is advertising our products and services. There are several damask patterns throughout the store. Our store's colors are blue, yellow, white, and gold.However the use of vibrant colors would be great! Our theme is old Hollywood. We have to use this design for our price list, product advertisement, and store promotions poster. Poster 2 and 3 can have the same layout. Poster 1 is different because I want the menu enclosed in a frame with the model resting against it or on top of it. All three posters will be hung on the same wall. I have attached my logo and additional photos for your review. I have also attached a images few posters. To give a better idea. I like how the fonts are not all the same. I like how they used the space. I like the use of color. Also I want the logo small with a white oval background. I don't want our logo to be a focal point.
Poster 1: The menu. This poster should include the blonde sailor either above the menu or beside the menu, 2 images have been included to choose from. I want the area with the prices in some type of decorative frame, with the model on top or on the side. (The model is displaying the prices) Also the model's background is white but I want her background to have color. Green would be great! I also like the idea of having "Now Showing" as part of the frame.
The text should read
" Services
Full Body Application..........................................$35.00
Half Body Application.........................................$20.00
Competition Application......................................$50,00
Face Only...........................................................$10.00
Packages:
4 Tans.... ............................................................$120.00 (Never Expires)
8 Tans ................................................................$200.00 (Never Expires)
Monthly Unlimited...............................................$95.00
Specials:
High School Students .......................................$25.00 EVERYDAY!!
All Day Every Tuesday.......................................$25.00
New Clients........................................................$25.00 (First Visit Only)
(If you want to be creative this section can be separate from the menu or part of the menu. Your choice)
Don't have time to come to us? We also have MOBILE Services! OUR ARTISTS CAN COME TO YOU!
In-Home Party Rates (5 people or more)...........$35.00 per person (Travel Fee Waived)
Poster 2: Kelvane Solution...The image of the pinup with the clock if for this poster.
The text should read:
" PRESSED FOR TIME? Try our KELVANE sunless solution. Rinse in as little as 2 hours" (Pressed for time, Kelvane, and 2 Hours is what we want to stand out)
Poster 3: Packages..The image for this poster is of the girl with the binoculars.
The text should read:
"We offer packages and memberships with UNBELIEVABLE SAVINGS. Tans as low as $20!!" (Unbelievable savings and $20 is what we want to stand out)
I made changes to my briefing. Please let me know if I need to make any other changes or additions
We increased our budget for our design, in order to get more participants
I updated our brief. I have included examples and more detailed instructions. I hope this helps
People who value beauty and glamour. We have an upscale clientele.
Advertising

```html
<!DOCTYPE html>
<html lang="en">
<head>
<meta charset="utf-8">
<title>Corvelle Beauty Lounge – Unbelievable Savings Poster</title>
<link href="https://fonts.googleapis.com/css2?family=Bangers&family=Exo+2:wght@500;700&display=swap" rel="stylesheet">
<style>
  :root {
    --board-light: #ffffff;
    --board-shade: #e4e4e6;
    --cream: #fdf6d6;
    --space-deep: #1a0e9e;
    --space-mid: #3a1fd8;
    --space-glow: #6a4bf0;
    --planet-1: #c44ee8;
    --planet-2: #4a22d8;
    --planet-rim: #f2c8ff;
    --model-skin: #e2b58c;
    --model-denim: #5575a8;
    --model-dress: #d8dceb;
    --headline: #f7f0a2;
    --headline-edge: #1b1466;
    --price-pink: #ec7fb8;
    --logo-ink: #6b2fa8;
    --ink-navy: #1d1a5a;
    --white: #ffffff;
  }
  * { box-sizing: border-box; margin: 0; padding: 0; }
  html, body { width: 1200px; height: 1000px; overflow: hidden; }
  body {
    background: radial-gradient(ellipse at 50% 45%, var(--board-light) 0%, var(--board-light) 45%, var(--board-shade) 100%);
    position: relative;
    font-family: "Exo 2", sans-serif;
  }
  .poster {
    position: absolute;
    left: 250px; top: 50px;
    width: 700px; height: 900px;
    background: var(--cream);
    box-shadow: 0 18px 30px rgba(0,0,0,0.22);
  }
  .poster__art {
    position: absolute;
    left: 10px; top: 10px;
    width: 680px; height: 836px;
    overflow: hidden;
    background: radial-gradient(ellipse at 70% 20%, var(--space-glow) 0%, var(--space-mid) 35%, var(--space-deep) 80%);
  }
  .poster__planet { position: absolute; inset: 0; }
  .poster__model {
    position: absolute;
    left: 0; top: 20px;
    width: 440px; height: 816px;
    border-radius: 200px 200px 0 0;
    background: linear-gradient(180deg, var(--model-skin) 0%, var(--model-skin) 30%, var(--model-denim) 48%, var(--model-denim) 60%, var(--model-dress) 78%, var(--model-dress) 100%);
    opacity: 0.85;
  }
  .offer {
    position: absolute;
    left: 292px; top: 66px;
    width: 300px;
    text-align: center;
    color: var(--white);
    text-shadow: 0 0 8px rgba(255,255,255,0.6);
  }
  .offer__lead { font-size: 36px; font-weight: 500; line-height: 1; }
  .offer__price { font-size: 62px; font-weight: 700; line-height: 1.05; }
  .offer__accent {
    position: absolute;
    left: 468px; top: 250px;
    font-family: "Bangers", sans-serif;
    font-size: 56px;
    color: var(--price-pink);
    transform: rotate(-6deg);
    letter-spacing: 1px;
  }
  .headline {
    position: absolute;
    left: 20px; top: 528px;
    width: 640px;
    text-align: center;
    font-family: "Bangers", sans-serif;
    font-weight: 400;
    color: var(--headline);
    -webkit-text-stroke: 3px var(--headline-edge);
    paint-order: stroke fill;
    text-shadow: 0 4px 0 var(--headline-edge);
    transform: rotate(-10deg);
    line-height: 0.95;
    letter-spacing: 2px;
  }
  .headline__top { font-size: 118px; display: block; }
  .headline__bottom { font-size: 118px; display: block; padding-left: 40px; }
  .brand {
    position: absolute;
    left: 450px; top: 728px;
    width: 130px; height: 50px;
    border-radius: 50%;
    background: var(--white);
    display: flex; align-items: center; justify-content: center;
    font-weight: 700;
    font-size: 19px;
    color: var(--logo-ink);
  }
  .tagline {
    position: absolute;
    left: 378px; top: 794px;
    width: 276px;
    padding: 2px 0;
    text-align: center;
    border: 1.5px solid var(--white);
    background: rgba(216,50,43,0.35);
    color: #ffd2cc;
    font-size: 13px;
    font-weight: 500;
    white-space: nowrap;
  }
  .poster__footer {
    position: absolute;
    left: 0; bottom: 0;
    width: 700px; height: 54px;
    display: flex; align-items: center; justify-content: center;
    font-size: 13px;
    font-weight: 500;
    color: var(--ink-navy);
  }
</style>
</head>
<body>
  <article class="poster">
    <div class="poster__art">
      <svg class="poster__planet" width="680" height="836" viewBox="0 0 680 836" aria-hidden="true">
        <defs>
          <linearGradient id="planetFill" x1="0" y1="0" x2="0" y2="1">
            <stop offset="0" stop-color="var(--planet-1)"/>
            <stop offset="0.35" stop-color="var(--planet-2)"/>
            <stop offset="1" stop-color="var(--space-deep)"/>
          </linearGradient>
        </defs>
        <ellipse cx="480" cy="1120" rx="900" ry="800" fill="url(#planetFill)" transform="rotate(-12 480 1120)"/>
        <ellipse cx="480" cy="1120" rx="900" ry="800" fill="none" stroke="var(--planet-rim)" stroke-opacity="0.6" stroke-width="5" transform="rotate(-12 480 1120)"/>
        <g fill="var(--white)" opacity="0.8">
          <circle cx="240" cy="40" r="1.5"/><circle cx="330" cy="140" r="1.2"/>
          <circle cx="610" cy="40" r="1.5"/><circle cx="650" cy="180" r="1.2"/>
          <circle cx="420" cy="220" r="1"/><circle cx="300" cy="60" r="1"/>
          <circle cx="520" cy="30" r="1.2"/><circle cx="660" cy="120" r="1"/>
        </g>
      </svg>
      <div class="poster__model" role="img" aria-label="Photo of a pin-up model in a bandana and denim dress looking through binoculars while holding a laptop"></div>
      <div class="offer">
        <p class="offer__lead">Tan as low as</p>
        <p class="offer__price">$20</p>
      </div>
      <p class="offer__accent">$20!</p>
      <h1 class="headline">
        <span class="headline__top">UNBELIEVABLE</span>
        <span class="headline__bottom">SAVINGS</span>
      </h1>
      <div class="brand">Corvelle</div>
      <p class="tagline">The Complete Body Airbrushing Company</p>
    </div>
    <p class="poster__footer">Don't have time to come to us? We also have MOBILE Services! OUR ARTISTS CAN COME TO YOU!</p>
  </article>
</body>
</html>
```